Box and label design for oil Tincture bottle

I need to design an attractive looking label for a 30ml CBD oil tincture along with designing a box for the tincture oil. I already have the logo (see attachment). I just need a nice, attractive looking artwork for the label and the box. The box is the standard 30ml tincture oil (see example attachment). The box has a total of 6 sides (4 on sides and 2 for top and bottom). Please include a section for supplemental facts and ingredients. Let's not focus to much on content. I am more concerned with design of box and label.
Target Market(s)
CBD customers

```html
<!DOCTYPE html>
<html lang="en">
<head>
<meta charset="utf-8">
<title>Bright Harbor CBD – Tincture Box and Bottle Label</title>
<link href="https://fonts.googleapis.com/css2?family=Barlow+Condensed:wght@500;600&family=Merriweather:wght@300;400&family=Open+Sans:wght@600&display=swap" rel="stylesheet">
<style>
  :root {
    --brand-blue: #0455a3;
    --sky: #8fd6ec;
    --leaf-light: #d9e6fb;
    --leaf-mid: #6f9ee8;
    --leaf-deep: #1d5fd0;
    --paper: #ffffff;
    --rule: #9a9a9a;
    --caption: #222222;
  }
  * { box-sizing: border-box; margin: 0; padding: 0; }
  html, body { width: 1200px; height: 837px; overflow: hidden; background: var(--paper); }
  .canvas { position: relative; width: 1200px; height: 837px; }
  .panel { position: absolute; }
  .blue { background: var(--brand-blue); }

  .heading { font-family: "Barlow Condensed", sans-serif; font-weight: 600; color: var(--brand-blue); text-transform: uppercase; }
  .body-copy { font-family: "Merriweather", serif; font-weight: 300; font-size: 7.3px; line-height: 1.42; }
  .wordmark { font-family: "Barlow Condensed", sans-serif; font-weight: 600; text-transform: uppercase; letter-spacing: .2px; white-space: nowrap; }
  .mark-circle { border-radius: 50%; border: 2px solid currentColor; }

  /* top flap */
  .flap-top { left: 235px; top: 55px; width: 154px; height: 155px; background: var(--sky); }
  .flap-top .inner { position: absolute; left: 11px; top: 11px; width: 132px; height: 132px; background: var(--brand-blue); }
  .flap-mark { position: absolute; inset: 0; display: flex; flex-direction: column; align-items: center; justify-content: center; gap: 6px; color: var(--paper); }
  .flap-mark .mark-circle { width: 56px; height: 56px; }
  .flap-mark .wordmark { font-size: 11px; }

  /* left side: directions */
  .side-info { left: 79px; top: 210px; width: 156px; height: 419px; border: 1px solid var(--rule); border-right: none; background: var(--paper); color: var(--brand-blue); }
  .side-info .block { position: absolute; left: 11px; width: 140px; }
  .side-info .heading { font-size: 10px; margin-bottom: 3px; }
  .side-info p { margin-bottom: 6px; }
  .side-info .gap { margin-top: 10px; }
  .side-leaf { position: absolute; left: 0; top: 213px; width: 125px; height: 185px; background: radial-gradient(ellipse at 50% 60%, var(--leaf-mid), var(--leaf-light) 70%, transparent 72%); }
  .side-footer { position: absolute; left: 0; right: 0; bottom: 8px; text-align: center; font-size: 9.5px; }

  /* front */
  .front { left: 235px; top: 210px; width: 154px; height: 419px; overflow: hidden; }
  .front-leaf-top { position: absolute; left: 0; top: 0; width: 34px; height: 180px; background: linear-gradient(180deg, rgba(255,255,255,.45), rgba(255,255,255,.15)); border-radius: 0 0 40px 0; }
  .front-leaf-main { position: absolute; left: 0; top: 170px; width: 154px; height: 249px; background: radial-gradient(ellipse at 60% 65%, rgba(255,255,255,.55), rgba(255,255,255,.12) 60%, transparent 72%); }
  .label-card { position: absolute; background: var(--paper); text-align: center; color: var(--brand-blue); }
  .front .label-card { left: 17px; top: 15px; width: 121px; height: 170px; }
  .card-mark { display: flex; flex-direction: column; align-items: center; gap: 4px; }
  .front .card-mark { padding-top: 22px; }
  .front .card-mark .mark-circle { width: 38px; height: 38px; }
  .front .card-mark .wordmark { font-size: 13px; }
  .product-kind { font-family: "Merriweather", serif; font-weight: 400; letter-spacing: 3px; }
  .product-name { font-family: "Barlow Condensed", sans-serif; font-weight: 600; line-height: 1; }
  .front .product-kind { font-size: 13px; margin-top: 26px; }
  .front .product-name { font-size: 27px; margin-top: 2px; }
  .dose-band { position: absolute; background: var(--sky); color: var(--brand-blue); font-family: "Merriweather", serif; font-weight: 400; display: flex; align-items: center; justify-content: center; white-space: nowrap; }
  .front .dose-band { left: 17px; top: 185px; width: 121px; height: 22px; font-size: 8px; }

  /* tagline side */
  .tagline-side { left: 389px; top: 210px; width: 155px; height: 419px; background: var(--paper); border-top: 1px solid var(--rule); border-bottom: 1px solid var(--rule); }
  .tagline { position: absolute; left: 50%; top: 50%; transform: translate(-50%, -50%) rotate(-90deg); font-size: 18.5px; letter-spacing: .3px; white-space: nowrap; }

  /* back */
  .back { left: 544px; top: 210px; width: 155px; height: 419px; overflow: hidden; color: var(--paper); }
  .back .body-copy { position: absolute; left: 12px; top: 43px; width: 136px; }
  .back .card-mark { position: absolute; left: 0; right: 0; top: 144px; }
  .back .card-mark .mark-circle { width: 38px; height: 38px; }
  .back .card-mark .wordmark { font-size: 13px; }
  .back-leaves { position: absolute; left: 0; top: 222px; width: 155px; height: 197px; background: radial-gradient(ellipse at 35% 70%, rgba(255,255,255,.5), transparent 55%), radial-gradient(ellipse at 80% 45%, rgba(40,110,230,.85), transparent 50%); }

  /* bottom flap */
  .flap-bottom { left: 235px; top: 629px; width: 154px; height: 156px; }
  .flap-bottom .flap-mark .mark-circle { width: 44px; height: 44px; }

  .caption { position: absolute; font-family: "Open Sans", sans-serif; font-weight: 600; font-size: 9.5px; color: var(--caption); letter-spacing: .4px; transform: translateX(-50%); white-space: nowrap; }

  /* bottle label */
  .bottle-label { left: 872px; top: 306px; width: 204px; height: 179px; overflow: hidden; }
  .bottle-leaf-left { position: absolute; left: 0; top: 8px; width: 55px; height: 130px; background: radial-gradient(ellipse at 40% 60%, rgba(40,110,230,.9), transparent 68%); }
  .bottle-leaf-right { position: absolute; right: 0; top: 30px; width: 58px; height: 149px; background: radial-gradient(ellipse at 60% 60%, rgba(255,255,255,.5), transparent 68%); }
  .bottle-label .label-card { left: 55px; top: 0; width: 94px; height: 132px; }
  .bottle-label .card-mark { padding-top: 17px; }
  .bottle-label .card-mark .mark-circle { width: 30px; height: 30px; }
  .bottle-label .card-mark .wordmark { font-size: 10.5px; }
  .bottle-label .product-kind { font-size: 10px; letter-spacing: 2.4px; margin-top: 15px; }
  .bottle-label .product-name { font-size: 19px; }
  .bottle-label .dose-band { left: 55px; top: 132px; width: 94px; height: 17px; font-size: 6.3px; }
</style>
</head>
<body>
<main class="canvas">

  <section class="panel flap-top" aria-label="Box top flap">
    <div class="inner">
      <div class="flap-mark"><span class="mark-circle"></span><span class="wordmark">Bright Harbor</span></div>
    </div>
  </section>

  <section class="panel side-info" aria-label="Box side: directions and ingredients">
    <div class="block body-copy" style="top:22px">
      <h2 class="heading">How to use</h2>
      <p>Lorem ipsum dolor sit amet, consetetuer adipiscing elit, sed diam nonummy nibh.</p>
      <p>Ut wisi enim ad minim veniam, quis nostrud exerci tation.</p>
      <p class="gap">Duis autem vel eum iriure dolor in hen-drerit in vulputate.</p>
    </div>
    <div class="block body-copy" style="top:139px">
      <h2 class="heading">Ingredients</h2>
      <p>CBD duis autem vel eum iriure dolor in hendrerit in vulputate velit esse mo-lestie consequat luptatum zzril.</p>
    </div>
    <div class="side-leaf" role="img" aria-label="Engraved hemp leaf illustration in blue"></div>
    <p class="heading side-footer">Bright Harbor CBD</p>
  </section>

  <section class="panel front blue" aria-label="Box front">
    <div class="front-leaf-top" role="img" aria-label="White engraved hemp leaf illustration"></div>
    <div class="front-leaf-main" role="img" aria-label="Large white engraved hemp leaf illustration"></div>
    <div class="label-card">
      <div class="card-mark"><span class="mark-circle"></span><span class="wordmark">Bright Harbor CBD</span></div>
      <p class="product-kind">CANNABIS</p>
      <h1 class="product-name">TINCTURE</h1>
    </div>
    <div class="dose-band">30 ml &nbsp;/&nbsp; 300mg of CBD</div>
  </section>

  <section class="panel tagline-side" aria-label="Box side: tagline">
    <p class="heading tagline">Tagline can go here tagline can go here</p>
  </section>

  <section class="panel back blue" aria-label="Box back">
    <p class="body-copy">Lorem ipsum dolor sit amet, consetetuer adipiscing elit, sed diam nonummy nibh euismod tincidunt ut laoreet dolorema na aliquam erat volutpat. Ut wisi enim ad minim veniam, quis nostrud exerci tation ullamcorper suscipit lobotis nisl ut aliquip ex ea.</p>
    <div class="card-mark"><span class="mark-circle"></span><span class="wordmark">Bright Harbor CBD</span></div>
    <div class="back-leaves" role="img" aria-label="White and bright blue engraved hemp leaf illustrations"></div>
  </section>

  <section class="panel flap-bottom blue" aria-label="Box bottom flap">
    <div class="flap-mark"><span class="mark-circle"></span><span class="wordmark">Bright Harbor</span></div>
  </section>

  <p class="caption" style="left:312px; top:800px">BOX DESIGN</p>

  <section class="panel bottle-label blue" aria-label="Bottle label">
    <div class="bottle-leaf-left" role="img" aria-label="Bright blue engraved hemp leaf illustration"></div>
    <div class="bottle-leaf-right" role="img" aria-label="White engraved hemp leaf illustration"></div>
    <div class="label-card">
      <div class="card-mark"><span class="mark-circle"></span><span class="wordmark">Bright Harbor CBD</span></div>
      <p class="product-kind">CANNABIS</p>
      <h2 class="product-name">TINCTURE</h2>
    </div>
    <div class="dose-band">30 ml &nbsp;/&nbsp; 300mg of CBD</div>
  </section>

  <p class="caption" style="left:974px; top:513px">BOTTLE LABEL DESIGN</p>

</main>
</body>
</html>
```